The Pixel Tap Business card.

A Simple card with our Logo and contact information. To give to investors and other professionals.

We are a nerd themed bar.
our target market is young professionals age 21+ but the real purpose of this business card is to present to potential investors and other professionals with our contact information. as we are still looking for funding before we start up.

I am partial to green and my partner likes red we are open to iteration.

Target Market(s)

Investors

Industry/Entity Type

Business

Contact Information for Business Card

Martin Hale (225) 730-6192 kent.h4711@mailnest.test Glen Porter (225) 968-5037 glenp318@mailnest.test

Font styles to use
Serif

Requirements
Nice to have
• Keep it simple but not boring.
• Use the Logos but feel free to edit them to match theme/colors.
• Keep the back clean and use one of the Logos.

```html
<!DOCTYPE html>
<html lang="en">
<head>
<meta charset="utf-8">
<title>The Pixel Tap – Business Card</title>
<link rel="stylesheet" href="https://fonts.googleapis.com/css2?family=Alegreya:wght@500;700&display=swap">
<style>
  :root {
    --backdrop: #e9e9ea;
    --wine-deep: #2e0204;
    --wine: #5a0408;
    --wine-light: #6e0a0e;
    --leaf: #4f7a16;
    --leaf-dark: #3c6210;
    --gold: #e9c86e;
    --gold-light: #f6e3a0;
    --gold-dark: #b3863a;
    --ink-gold: #d7ad62;
  }
  * { box-sizing: border-box; margin: 0; padding: 0; }
  html, body { width: 1200px; height: 800px; overflow: hidden; }
  body {
    background: var(--backdrop);
    font-family: "Alegreya", Georgia, serif;
    position: relative;
  }
  .card {
    position: absolute;
    top: 251px;
    width: 520px;
    height: 297px;
    overflow: hidden;
    box-shadow: 0 10px 28px rgba(0,0,0,.22);
  }
  .card--front { left: 50px; }
  .card--back { left: 630px; }
  .card__art { position: absolute; inset: 0; width: 100%; height: 100%; }

  .brand {
    position: absolute;
    color: var(--ink-gold);
    font-weight: 700;
    text-transform: uppercase;
    letter-spacing: .02em;
    line-height: 1;
    display: flex;
    align-items: center;
    gap: 10px;
  }
  .brand__dot {
    width: 14px; height: 14px;
    border-radius: 50%;
    background: var(--ink-gold);
  }
  .tagline {
    position: absolute;
    color: var(--ink-gold);
    font-weight: 500;
    font-size: 10px;
    letter-spacing: .12em;
    text-transform: uppercase;
  }
  .card--front .brand { left: 40px; top: 58px; font-size: 32px; }
  .card--front .tagline { left: 66px; top: 96px; }
  .card--back .brand { left: 118px; top: 122px; font-size: 34px; }
  .card--back .tagline { left: 144px; top: 162px; }

  .contact {
    position: absolute;
    color: var(--ink-gold);
    font-size: 13px;
    line-height: 1.35;
    font-weight: 500;
  }
  .contact__name { font-size: 19px; font-weight: 700; line-height: 1.2; }
  .contact--first { left: 40px; top: 128px; }
  .contact--second { left: 286px; top: 196px; }
</style>
</head>
<body>

<section class="card card--front" aria-label="Business card front">
  <svg class="card__art" viewBox="0 0 520 297" preserveAspectRatio="none" aria-hidden="false">
    <defs>
      <radialGradient id="wineFront" cx="0.35" cy="0.45" r="0.9">
        <stop offset="0" stop-color="#6a080d"/>
        <stop offset="1" stop-color="#2a0103"/>
      </radialGradient>
      <linearGradient id="goldFront" x1="0" y1="0" x2="1" y2="1">
        <stop offset="0" stop-color="#b3863a"/>
        <stop offset=".45" stop-color="#f6e3a0"/>
        <stop offset="1" stop-color="#c79a48"/>
      </linearGradient>
    </defs>
    <rect class="card__field" width="520" height="297" fill="url(#wineFront)"/>
    <path role="img" aria-label="Green panel with a gold damask pattern"
          d="M190,0 C300,18 350,110 410,185 C450,232 485,255 520,262 L520,0 Z"
          fill="#4f7a16"/>
    <path class="card__rule" d="M182,2 C292,22 342,114 402,190 C442,238 480,262 520,270"
          fill="none" stroke="#5a0408" stroke-width="4"/>
    <path class="card__band" d="M190,0 C300,18 350,110 410,185 C450,232 485,255 520,262"
          fill="none" stroke="url(#goldFront)" stroke-width="9"/>
  </svg>

  <div class="brand">The Pixel Tap</div>
  <div class="tagline">Lounge and Arcade</div>

  <div class="contact contact--first">
    <div class="contact__name">Martin Hale</div>
    <div>Phone: (225) 730-6192</div>
    <div>Email: kent.h4711@mailnest.test</div>
  </div>
  <div class="contact contact--second">
    <div class="contact__name">Glen Porter</div>
    <div>Phone: (225) 968-5037</div>
    <div>Email: glenp318@mailnest.test</div>
  </div>
</section>

<section class="card card--back" aria-label="Business card back">
  <svg class="card__art" viewBox="0 0 520 297" preserveAspectRatio="none">
    <defs>
      <radialGradient id="wineBack" cx="0.4" cy="0.5" r="0.8">
        <stop offset="0" stop-color="#6a080d"/>
        <stop offset="1" stop-color="#2a0103"/>
      </radialGradient>
      <linearGradient id="goldBack" x1="0" y1="0" x2="1" y2="0">
        <stop offset="0" stop-color="#c79a48"/>
        <stop offset=".5" stop-color="#f6e3a0"/>
        <stop offset="1" stop-color="#b3863a"/>
      </linearGradient>
    </defs>
    <rect role="img" aria-label="Green field with a gold damask pattern"
          width="520" height="297" fill="#4f7a16"/>
    <path class="card__field"
          d="M0,30 C150,42 360,18 520,48 L520,262 C360,236 150,258 0,248 Z"
          fill="url(#wineBack)"/>
    <path d="M0,22 C150,34 360,10 520,40" fill="none" stroke="#5a0408" stroke-width="4"/>
    <path d="M0,30 C150,42 360,18 520,48" fill="none" stroke="url(#goldBack)" stroke-width="8"/>
    <path d="M0,248 C150,258 360,236 520,262" fill="none" stroke="url(#goldBack)" stroke-width="8"/>
    <path d="M0,256 C150,266 360,244 520,270" fill="none" stroke="#5a0408" stroke-width="4"/>
  </svg>

  <div class="brand"><span class="brand__dot"></span>The Pixel Tap</div>
  <div class="tagline">Lounge and Arcade</div>
</section>

</body>
</html>
```